Kestrolan - Home Loans

We need a DL sized (214mm x 103mm) flyer to be designed for our mortgage broking arm of the business. We want something that prospective clients can pick up and remind them to review their current interest rates, potentially save thousands of dollars over the life of the loan. Or for those who are currently in the market for a new property - just to let them know we can potentially compare over 30 lenders to identify the right loan for them.

Designs to be in shades of green - refer to our website: www.kestrolan.com.au/
Logos attached also.

Industry/Entity Type

Loan

```html
<!DOCTYPE html>
<html lang="en">
<head>
<meta charset="utf-8">
<title>Kestrolan – Mortgages</title>
<link href="https://fonts.googleapis.com/css2?family=Carlito:wght@400;700&display=swap" rel="stylesheet">
<style>
  :root {
    --lime: #d3e637;
    --lime-soft: #e4f07a;
    --lime-deep: #b8d020;
    --bar-edge: #5c6b10;
    --ink: #777777;
    --ink-dark: #1f2412;
    --paper: #ffffff;
    --mint: #cfe8c4;
    --mint-fade: #eef7ea;
  }
  * { margin: 0; padding: 0; box-sizing: border-box; }
  html, body { width: 1200px; height: 2493px; overflow: hidden; background: var(--paper); }
  .flyer {
    position: relative;
    width: 1200px;
    height: 2493px;
    background: var(--paper);
    font-family: "Carlito", "Calibri", sans-serif;
  }
  .title-band {
    position: absolute;
    left: 0; top: 117px;
    width: 1200px; height: 260px;
    background: var(--lime);
  }
  .title-band__text {
    position: absolute;
    left: 17px; top: 68px;
    font-size: 110px;
    line-height: 1;
    color: var(--paper);
    letter-spacing: 1px;
  }
  .advisor-photo {
    position: absolute;
    left: 790px; top: 0;
    width: 360px; height: 403px;
    background: linear-gradient(160deg, #f2a46a 0%, #e8782a 45%, #eeeeee 75%, #ffffff 100%);
    border-radius: 0 0 12px 12px;
  }
  .body-copy {
    position: absolute;
    left: 51px;
    width: 1120px;
    font-size: 62px;
    line-height: 89px;
    color: var(--ink);
  }
  .body-copy--intro { top: 546px; }
  .body-copy--more { top: 1254px; }
  .family-photo {
    position: absolute;
    left: 103px; top: 1714px;
    width: 994px; height: 574px;
    background: radial-gradient(ellipse at 50% 70%, var(--mint) 0%, #dff0d8 55%, var(--mint-fade) 80%, var(--paper) 100%);
    border-radius: 300px 300px 0 0;
  }
  .footer-bar {
    position: absolute;
    left: 0; top: 2288px;
    width: 1200px; height: 205px;
    background: linear-gradient(180deg, var(--lime-soft) 0%, var(--lime) 45%, var(--lime-deep) 100%);
    border-top: 5px solid var(--bar-edge);
    border-bottom: 5px solid var(--bar-edge);
  }
  .brand {
    position: absolute;
    left: 214px; top: 0;
    height: 195px;
    display: flex;
    align-items: center;
    gap: 36px;
  }
  .brand__mark {
    width: 118px; height: 118px;
    background: var(--ink-dark);
    border-radius: 50%;
  }
  .brand__name {
    font-size: 110px;
    line-height: 1;
    color: var(--ink-dark);
    letter-spacing: 2px;
    text-transform: uppercase;
  }
</style>
</head>
<body>
<main class="flyer">
  <div class="title-band">
    <h1 class="title-band__text">MORTGAGES</h1>
  </div>
  <div class="advisor-photo" role="img" aria-label="Smiling mortgage adviser leaning on a rising bar chart"></div>

  <p class="body-copy body-copy--intro">Work with our mortgage brokers to<br>find the right lender and home loan<br>for your next property purchase.<br>With access to the most competitive<br>interest rates from over 30 lenders,<br>we will negotiate the best deal for<br>your mortgage.</p>

  <p class="body-copy body-copy--more">What’s more, we’ll show you how to<br>save tens of thousands in interest on<br>your primary residence, and help you<br>grow your property portfolio faster.</p>

  <div class="family-photo" role="img" aria-label="Happy young family with a child, softly faded in green"></div>

  <footer class="footer-bar">
    <div class="brand">
      <span class="brand__mark"></span>
      <span class="brand__name">Kestrolan</span>
    </div>
  </footer>
</main>
</body>
</html>
```